I need a business card design for: Brindle Financial Solutions. Logo design has been attached. I will also need the business address: 84 West Harrow St. Suite 410C Harlow Springs, PA 15990. Phone and Fax : 555-318-0947 (phone) and 555-318-0949 (fax). Email address: tbrindle@brindlefinancialsolutions.example. Please add my title: Financial Advisor.
The following disclosure must appear on business card, letterhead, and stationary: Securities and investment advisory services offered through LPD Holdings Corporation (LPD) member QOTEB/WAHL. LPD is separately owned and other entities and/or marketing names, products or services referenced here are independent of LPD.

```html
<!DOCTYPE html>
<html lang="en">
<head>
<meta charset="utf-8">
<title>Brindle Financial Solutions – Business Card</title>
<link rel="stylesheet" href="https://fonts.googleapis.com/css2?family=Montserrat:wght@600&family=Arimo:wght@400&display=swap">
<style>
  :root {
    --backdrop: #29292b;
    --card: #0c0c0d;
    --brand-blue: #0f4e96;
    --text-light: #d2d2d2;
    --text-muted: #a9a9a9;
    --rule: #3a3a3c;
  }
  * { box-sizing: border-box; margin: 0; padding: 0; }
  html, body { width: 1200px; height: 900px; overflow: hidden; }
  body {
    background: var(--backdrop);
    font-family: "Arimo", Arial, sans-serif;
    display: flex;
    flex-direction: column;
    align-items: center;
    justify-content: center;
    gap: 40px;
  }
  .card {
    width: 630px;
    height: 360px;
    background: var(--card);
    position: relative;
    box-shadow: 0 10px 30px rgba(0,0,0,.45);
  }
  .brand-name {
    font-family: "Montserrat", Arial, sans-serif;
    font-weight: 600;
    color: var(--brand-blue);
    text-transform: uppercase;
    letter-spacing: 1.5px;
    text-align: center;
    line-height: 1.25;
  }
  /* Front */
  .card-front { display: flex; }
  .front-brand {
    width: 280px;
    display: flex;
    align-items: center;
    justify-content: center;
    padding: 0 30px;
  }
  .front-brand .brand-name { font-size: 20px; }
  .front-divider {
    width: 1px;
    background: var(--rule);
    margin: 50px 0;
  }
  .front-details {
    flex: 1;
    padding: 62px 0 0 34px;
    color: var(--text-light);
  }
  .person-name {
    font-family: "Montserrat", Arial, sans-serif;
    font-weight: 600;
    font-size: 24px;
    color: var(--brand-blue);
    text-transform: uppercase;
    letter-spacing: .5px;
  }
  .person-title { font-size: 15px; margin-top: 2px; margin-bottom: 14px; }
  .contact-list { list-style: none; font-size: 14px; line-height: 22px; }
  .contact-list li { display: flex; align-items: center; gap: 8px; white-space: nowrap; }
  .contact-icon { width: 14px; height: 14px; fill: var(--brand-blue); flex-shrink: 0; }
  .web-domain { color: var(--brand-blue); }
  .address { font-size: 15px; line-height: 22px; margin-top: 16px; }
  /* Back */
  .card-back {
    display: flex;
    flex-direction: column;
    align-items: center;
    justify-content: center;
    padding: 0 50px;
  }
  .card-back .brand-name { font-size: 32px; margin-bottom: 46px; }
  .disclosure {
    font-size: 11px;
    line-height: 16px;
    color: var(--text-muted);
    text-align: center;
  }
</style>
</head>
<body>

  <section class="card card-front" aria-label="Business card front">
    <div class="front-brand">
      <p class="brand-name">Brindle Financial Solutions</p>
    </div>
    <div class="front-divider"></div>
    <div class="front-details">
      <h1 class="person-name">Thomas Brindle</h1>
      <p class="person-title">Financial Advisor</p>
      <ul class="contact-list">
        <li>
          <svg class="contact-icon" viewBox="0 0 16 16" aria-hidden="true"><path d="M3.6 1.5l2.3 2.6-1.3 1.9c.9 2 2.5 3.6 4.6 4.6l1.9-1.3 2.6 2.3-1.3 2.2C7.5 15.3 .7 8.5 1.4 2.8z"/></svg>
          555-318-0947
        </li>
        <li>
          <svg class="contact-icon" viewBox="0 0 16 16" aria-hidden="true"><path d="M4 1h8v4H4zM1 6h14v6h-3v3H4v-3H1zm4 4v4h6v-4z"/></svg>
          555-318-0949
        </li>
        <li>
          <svg class="contact-icon" viewBox="0 0 16 16" aria-hidden="true"><path d="M1 3h14v10H1zm1.5 1.2L8 8.6l5.5-4.4z"/></svg>
          tbrindle@brindlefinancialsolutions.example
        </li>
        <li>
          <svg class="contact-icon" viewBox="0 0 16 16" aria-hidden="true"><path d="M8 1a7 7 0 100 14A7 7 0 008 1zm-1 2.2V7H3.1A5 5 0 017 3.2zm2 0A5 5 0 0112.9 7H9zM3.1 9H7v3.8A5 5 0 013.1 9zM9 9h3.9A5 5 0 019 12.8z"/></svg>
          <span>www.<span class="web-domain">brindlefinancialsolutions</span>.example</span>
        </li>
      </ul>
      <p class="address">84 West Harrow St. Suite<br>410C Harlow Springs, PA 15990.</p>
    </div>
  </section>

  <section class="card card-back" aria-label="Business card back">
    <p class="brand-name">Brindle Financial Solutions</p>
    <p class="disclosure">Securities and investment advisory services offered through LPD Holdings Corporation (LPD) member<br>QOTEB/WAHL. LPD is separately owned and other entities and/or marketing names,<br>products or services referenced here are independent of LPD</p>
  </section>

</body>
</html>
```